Website For Custom Home Builder

-Very elegant and simple design as I am a high end custom home builder.
-I build homes $2 million to $10 million range so the website needs to reflect the level of home that I build.
-Attached are photos of homes I have built to use as well as my logo.
-I need final design to be in layered format so my local guy can edit if he needs to.

3 Page Design
1. HomePage:
-logo, some photos,
-“Building beautiful custom homes in Indianapolis for over 20 years”
2. AboutPage:
-Wade Holloran has been building stunning custom homes in the Indianpolis area for over 20 years. As a small boutique building company we only build a handful of homes a year in order to offer our clients the personal attention that their homes deserve. It's this attention to detail that makes our client experience and final product something special and unique.
- family photo
3. ContactPage:
-office photo
-317-552-7190
-wade@whcrafted.com
-415 North Fernmill Rd, Suite 308, Carmel IN 46033

Target Market(s)

Very high end clients looking to build $2 million to $10 million homes.

Industry/Entity Type

Residential high end custom home builder/construction

Coding

Coded - Design and coding required

Number of Pages Required

3 page

Requirements
Must have
• Very simple and elegant design that represents the high end homes that I build.
Nice to have
Should not have
• Should NOT have a lot of clutter or be a very busy page from a design perspective.

```html
<!DOCTYPE html>
<html lang="en">
<head>
<meta charset="utf-8">
<title>Wade Holloran Custom Homes — Website Pages</title>
<link href="https://fonts.googleapis.com/css2?family=Source+Sans+3:wght@400;600;700&display=swap" rel="stylesheet">
<style>
  :root{
    --brown:#5a2a12;
    --brown-mid:#7a3c1c;
    --brown-light:#9a5630;
    --footer:#250c03;
    --footer-bar:#3a1508;
    --ink:#1c120d;
    --muted:#6b5a50;
    --peach:#f8e6da;
    --card:#ffffff;
    --line:#e9ddd4;
    --photo-warm:#b98a66;
  }
  *{box-sizing:border-box;margin:0;padding:0}
  html,body{width:1200px;height:822px;overflow:hidden;background:#fff}
  body{font-family:"Source Sans 3",sans-serif;color:var(--ink)}
  .board{position:absolute;left:0;top:0;width:2320px;height:1590px;transform:scale(0.51724);transform-origin:0 0}
  .page{position:absolute;background:linear-gradient(#fff,#fdf7f3 60%,#fff);box-shadow:0 0 6px rgba(0,0,0,.12);overflow:hidden}
  .page-home{left:24px;top:57px;width:744px;height:1480px}
  .page-about{left:789px;top:57px;width:745px;height:1090px}
  .page-contact{left:1558px;top:57px;width:738px;height:753px}
  .abs{position:absolute}

  /* header */
  .site-header{position:absolute;left:0;top:0;width:100%;height:82px;background:linear-gradient(90deg,var(--peach),#fff 70%)}
  .brand{position:absolute;left:100px;top:40px;display:flex;align-items:center;gap:8px}
  .brand-square{width:12px;height:12px;background:var(--brown)}
  .brand-name{font-size:18px;font-weight:600;letter-spacing:.5px;color:var(--brown)}
  .top-contact{position:absolute;left:455px;top:24px;display:flex;gap:14px;font-size:8.5px;color:var(--ink)}
  .top-contact span{display:flex;align-items:center;gap:5px}
  .ico{width:10px;height:10px;background:var(--brown);display:inline-flex;align-items:center;justify-content:center}
  .ico svg{width:7px;height:7px}
  .main-nav{position:absolute;left:370px;top:59px;display:flex;gap:15px;font-size:9px;font-weight:600;color:var(--ink)}
  .main-nav .active{color:var(--brown-light)}

  .section-title{position:absolute;left:0;width:100%;text-align:center;font-weight:700;font-size:21px;letter-spacing:.3px;color:var(--ink)}

  /* photo placeholders */
  .photo{position:absolute}
  .framed{border:4px solid #fff;box-shadow:0 0 4px rgba(0,0,0,.3)}

  /* reviews */
  .review{position:absolute;width:173px;height:145px;background:var(--card);box-shadow:0 1px 4px rgba(0,0,0,.1);padding:12px 10px}
  .review-head{display:flex;align-items:center;gap:7px}
  .avatar{width:26px;height:26px;border-radius:50%;background:linear-gradient(#8d6a55,#4a5a4e)}
  .review-name{font-size:10.5px;font-weight:700;line-height:1}
  .review-role{font-size:6.5px;color:var(--muted)}
  .quote-mark{position:absolute;right:10px;top:4px;font-size:34px;font-weight:700;color:#d9d2cd;line-height:1}
  .stars{margin-top:8px;font-size:13px;letter-spacing:2px;color:var(--brown)}
  .review-text{margin-top:8px;font-size:6.8px;line-height:1.7;text-align:justify;color:var(--ink)}

  /* footer */
  .site-footer{position:absolute;left:0;width:100%;background:var(--footer);color:#fff}
  .footer-brand{position:absolute;left:100px;top:118px;display:flex;align-items:center;gap:10px}
  .footer-brand .brand-square{width:18px;height:18px;background:#fff}
  .footer-brand .brand-name{color:#fff;font-size:28px;font-weight:600}
  .footer-col-title{font-size:11px;font-weight:600;margin-bottom:14px}
  .quick-links{position:absolute;left:350px;top:48px}
  .quick-links li{list-style:none;font-size:7.5px;font-weight:600;margin-bottom:8.6px}
  .footer-contact{position:absolute;left:474px;top:48px}
  .footer-row{display:flex;gap:10px;margin-bottom:12px}
  .footer-row .ico{width:16px;height:16px;background:transparent;border:1px solid #fff;margin-top:2px}
  .footer-row .ico svg{width:9px;height:9px}
  .f-label{font-size:8px;font-weight:600;line-height:1}
  .f-value{font-size:10.5px;font-weight:600;line-height:1.2}
  .footer-bar{position:absolute;left:0;bottom:0;width:100%;height:42px;background:var(--footer-bar);font-size:7.5px;font-weight:600;display:flex;align-items:center;justify-content:center}
</style>
</head>
<body>
<svg width="0" height="0" style="position:absolute">
  <defs>
    <symbol id="i-mail" viewBox="0 0 10 10"><rect x="1" y="2.5" width="8" height="5.5" fill="none" stroke="#fff" stroke-width="1"/><path d="M1 2.8 5 5.8 9 2.8" fill="none" stroke="#fff" stroke-width="1"/></symbol>
    <symbol id="i-phone" viewBox="0 0 10 10"><path d="M2 1.5h2l.8 2-1.2.9a5 5 0 0 0 2 2l.9-1.2 2 .8v2c0 .5-.5 1-1 1A7 7 0 0 1 1 2.5c0-.5.5-1 1-1z" fill="none" stroke="#fff" stroke-width=".9"/></symbol>
    <symbol id="i-pin" viewBox="0 0 10 10"><path d="M5 9.2S2 6 2 4a3 3 0 0 1 6 0c0 2-3 5.2-3 5.2z" fill="none" stroke="#fff" stroke-width=".9"/><circle cx="5" cy="4" r="1" fill="#fff"/></symbol>
  </defs>
</svg>

<div class="board">

  <!-- HOME PAGE -->
  <section class="page page-home">
    <header class="site-header">
      <div class="brand"><span class="brand-square"></span><span class="brand-name">WADE HOLLORAN</span></div>
      <div class="top-contact">
        <span><i class="ico"><svg><use href="#i-mail"/></svg></i>wade@whcrafted.com</span>
        <span><i class="ico"><svg><use href="#i-phone"/></svg></i>317-552-7190</span>
      </div>
      <nav class="main-nav"><span class="active">HOME</span><span>ABOUT</span><span>PROPERTIES</span><span>NEWS</span><span>BLOG</span><span>CONTACT</span></nav>
    </header>

    <div class="abs" style="left:120px;top:113px;width:246px;height:380px;border:1px solid #bbb"></div>
    <div class="abs" style="left:190px;top:122px;width:247px;height:371px;background:var(--brown-mid)"></div>
    <div class="abs" style="left:280px;top:184px;width:190px;height:300px;border:1.5px solid var(--brown)"></div>
    <div class="photo" role="img" aria-label="Modern home office with large window, wood desk and leather chair" style="left:40px;top:145px;width:410px;height:323px;background:linear-gradient(100deg,#3e3f44 0 14%,#8fa27a 14% 45%,#cfc6ba 45% 70%,#7a5a3d 70%)"></div>
    <div class="abs" style="left:320px;top:285px;width:384px;height:91px;background:linear-gradient(90deg,var(--brown),var(--brown-light));display:flex;align-items:center;justify-content:center;gap:12px">
      <span style="width:16px;height:16px;background:#fff"></span>
      <span style="color:#fff;font-size:40px;font-weight:600;letter-spacing:1px">WADE HOLLORAN</span>
    </div>
    <div class="abs" style="left:600px;top:414px;display:flex;gap:5px">
      <i style="width:7px;height:7px;border-radius:50%;background:#777"></i><i style="width:7px;height:7px;border-radius:50%;background:#ccc"></i><i style="width:7px;height:7px;border-radius:50%;background:#ccc"></i><i style="width:7px;height:7px;border-radius:50%;background:#ccc"></i>
    </div>

    <h1 class="section-title" style="top:562px;font-size:20.5px;line-height:1.15">BUILDING BEAUTIFUL CUSTOM HOMES IN INDIANAPOLIS<br>FOR OVER 20 YEARS</h1>

    <div class="photo framed" role="img" aria-label="Backyard pool at dusk" style="left:20px;top:680px;width:86px;height:198px;background:linear-gradient(#6b6a5a,#3c4a3a 60%,#2d6fa8)"></div>
    <div class="photo framed" role="img" aria-label="Lit patio and pool at night" style="left:638px;top:680px;width:86px;height:198px;background:linear-gradient(#3a3430,#8a5a34 50%,#1f5f9a)"></div>
    <div class="photo framed" role="img" aria-label="Stone and timber custom home at sunset" style="left:100px;top:630px;width:544px;height:296px;background:linear-gradient(#c89460,#e7b27a 22%,#6d6256 45%,#54483f 70%,#4d6a34)"></div>

    <h2 class="section-title" style="top:975px">CUSTOM HOMES</h2>

    <article class="review" style="left:100px;top:1025px"><div class="review-head"><span class="avatar" role="img" aria-label="Client portrait"></span><div><div class="review-name">ROBOTO DOSE</div><div class="review-role">Client</div></div></div><span class="quote-mark">”</span><div class="stars">★★★★★</div><p class="review-text">“Phasellus aliquam quis lorem amet dapibus feugiat vitae purus vitae efficitur. Vestibulum sed elit id orci rhoncus ultricies. Morbi vitae semper consequat ipsum semper quam”.</p></article>
    <article class="review" style="left:285px;top:1025px"><div class="review-head"><span class="avatar" role="img" aria-label="Client portrait"></span><div><div class="review-name">BRAITLY DISOCA</div><div class="review-role">Client</div></div></div><span class="quote-mark">”</span><div class="stars">★★★★★</div><p class="review-text">“Phasellus aliquam quis lorem amet dapibus feugiat vitae purus vitae efficitur. Vestibulum sed elit id orci rhoncus ultricies. Morbi vitae semper consequat ipsum semper quam”.</p></article>
    <article class="review" style="left:469px;top:1025px"><div class="review-head"><span class="avatar" role="img" aria-label="Client portrait"></span><div><div class="review-name">JINA NILSON</div><div class="review-role">Client</div></div></div><span class="quote-mark">”</span><div class="stars">★★★★★</div><p class="review-text">“Phasellus aliquam quis lorem amet dapibus feugiat vitae purus vitae efficitur. Vestibulum sed elit id orci rhoncus ultricies. Morbi vitae semper consequat ipsum semper quam”.</p></article>

    <footer class="site-footer" style="top:1223px;height:257px">
      <div class="footer-brand"><span class="brand-square"></span><span class="brand-name">WADE HOLLORAN</span></div>
      <div class="quick-links"><div class="footer-col-title">QUICK LINKS</div><ul><li>HOME</li><li>ABOUT</li><li>PROPERTIES</li><li>NEWS</li><li>BLOG</li><li>CONTACT</li></ul></div>
      <div class="footer-contact"><div class="footer-col-title">CONTACT US</div>
        <div class="footer-row"><i class="ico"><svg><use href="#i-phone"/></svg></i><div><div class="f-label">PHONE:</div><div class="f-value">317-552-7190</div></div></div>
        <div class="footer-row"><i class="ico"><svg><use href="#i-mail"/></svg></i><div><div class="f-label">MAIL:</div><div class="f-value">wade@whcrafted.com</div></div></div>
        <div class="footer-row"><i class="ico"><svg><use href="#i-pin"/></svg></i><div><div class="f-label">MAIL:</div><div class="f-value">415 North Fernmill Rd,<br>Suite 308, Carmel IN 46033</div></div></div>
      </div>
      <div class="footer-bar">COPYRIGHT © WADE HOLLORAN 2023 . ALL RIGHTS RESERVED.</div>
    </footer>
  </section>

  <!-- ABOUT PAGE -->
  <section class="page page-about">
    <header class="site-header">
      <div class="brand"><span class="brand-square"></span><span class="brand-name">WADE HOLLORAN</span></div>
      <div class="top-contact">
        <span><i class="ico"><svg><use href="#i-mail"/></svg></i>wade@whcrafted.com</span>
        <span><i class="ico"><svg><use href="#i-phone"/></svg></i>317-552-7190</span>
      </div>
      <nav class="main-nav"><span>HOME</span><span class="active">ABOUT</span><span>PROPERTIES</span><span>NEWS</span><span>BLOG</span><span>CONTACT</span></nav>
    </header>

    <h1 class="section-title" style="top:118px">ABOUT US</h1>
    <div class="photo framed" role="img" aria-label="Team group photo in a bright office lobby" style="left:100px;top:163px;width:545px;height:297px;background:linear-gradient(#e3e1dc,#c9c4bd 45%,#2f3448 75%,#25293a)"></div>
    <p class="abs" style="left:100px;top:486px;width:545px;font-size:9.3px;line-height:1.55;text-align:center">Wade Holloran has been building stunning custom homes in the Indianapolis area for over 20 years. As a small boutique building company we only build a handful of homes a year in order to offer our clients the personal attention that their homes deserve. It's this attention to detail that makes our client experience and final product something special and unique.</p>

    <h2 class="section-title" style="top:582px">CUSTOMER REVIEWS</h2>
    <article class="review" style="left:100px;top:634px"><div class="review-head"><span class="avatar" role="img" aria-label="Client portrait"></span><div><div class="review-name">ROBOTO DOSE</div><div class="review-role">Client</div></div></div><span class="quote-mark">”</span><div class="stars">★★★★★</div><p class="review-text">“Phasellus aliquam quis lorem amet dapibus feugiat vitae purus vitae efficitur. Vestibulum sed elit id orci rhoncus ultricies. Morbi vitae semper consequat ipsum semper quam”.</p></article>
    <article class="review" style="left:285px;top:634px"><div class="review-head"><span class="avatar" role="img" aria-label="Client portrait"></span><div><div class="review-name">BRAITLY DISOCA</div><div class="review-role">Client</div></div></div><span class="quote-mark">”</span><div class="stars">★★★★★</div><p class="review-text">“Phasellus aliquam quis lorem amet dapibus feugiat vitae purus vitae efficitur. Vestibulum sed elit id orci rhoncus ultricies. Morbi vitae semper consequat ipsum semper quam”.</p></article>
    <article class="review" style="left:469px;top:634px"><div class="review-head"><span class="avatar" role="img" aria-label="Client portrait"></span><div><div class="review-name">JINA NILSON</div><div class="review-role">Client</div></div></div><span class="quote-mark">”</span><div class="stars">★★★★★</div><p class="review-text">“Phasellus aliquam quis lorem amet dapibus feugiat vitae purus vitae efficitur. Vestibulum sed elit id orci rhoncus ultricies. Morbi vitae semper consequat ipsum semper quam”.</p></article>

    <footer class="site-footer" style="top:835px;height:255px">
      <div class="footer-brand"><span class="brand-square"></span><span class="brand-name">WADE HOLLORAN</span></div>
      <div class="quick-links"><div class="footer-col-title">QUICK LINKS</div><ul><li>HOME</li><li>ABOUT</li><li>PROPERTIES</li><li>NEWS</li><li>BLOG</li><li>CONTACT</li></ul></div>
      <div class="footer-contact"><div class="footer-col-title">CONTACT US</div>
        <div class="footer-row"><i class="ico"><svg><use href="#i-phone"/></svg></i><div><div class="f-label">PHONE:</div><div class="f-value">317-552-7190</div></div></div>
        <div class="footer-row"><i class="ico"><svg><use href="#i-mail"/></svg></i><div><div class="f-label">MAIL:</div><div class="f-value">wade@whcrafted.com</div></div></div>
        <div class="footer-row"><i class="ico"><svg><use href="#i-pin"/></svg></i><div><div class="f-label">MAIL:</div><div class="f-value">415 North Fernmill Rd,<br>Suite 308, Carmel IN 46033</div></div></div>
      </div>
      <div class="footer-bar">COPYRIGHT © WADE HOLLORAN 2023 . ALL RIGHTS RESERVED.</div>
    </footer>
  </section>

  <!-- CONTACT PAGE -->
  <section class="page page-contact">
    <header class="site-header">
      <div class="brand"><span class="brand-square"></span><span class="brand-name">WADE HOLLORAN</span></div>
      <div class="top-contact">
        <span><i class="ico"><svg><use href="#i-mail"/></svg></i>wade@whcrafted.com</span>
        <span><i class="ico"><svg><use href="#i-phone"/></svg></i>317-552-7190</span>
      </div>
      <nav class="main-nav" style="left:366px"><span>HOME</span><span>ABOUT</span><span>PROPERTIES</span><span>NEWS</span><span>BLOG</span><span class="active">CONTACT</span></nav>
    </header>

    <h1 class="section-title" style="top:117px">CONTACT US</h1>
    <div class="abs" style="left:100px;top:166px;width:538px;height:275px;background:#fff;box-shadow:0 1px 5px rgba(0,0,0,.08)"></div>
    <div class="photo" role="img" aria-label="Modern kitchen with white cabinets, marble island and walnut accents" style="left:110px;top:177px;width:227px;height:254px;background:linear-gradient(#e8e6e2,#cfcac3 45%,#8a5a36 65%,#5a3a24)"></div>
    <div class="abs" style="left:360px;top:242px;font-size:16px;font-weight:700">GET IN TOUCH</div>
    <div class="abs" style="left:360px;top:278px">
      <div class="footer-row" style="margin-bottom:16px"><i class="ico" style="width:24px;height:24px"><svg style="width:13px;height:13px"><use href="#i-phone"/></svg></i><div><div style="font-size:11.5px;font-weight:600;line-height:1">PHONE:</div><div style="font-size:15px;font-weight:600">317-552-7190</div></div></div>
      <div class="footer-row" style="margin-bottom:16px"><i class="ico" style="width:24px;height:24px"><svg style="width:13px;height:13px"><use href="#i-mail"/></svg></i><div><div style="font-size:11.5px;font-weight:600;line-height:1">MAIL:</div><div style="font-size:15px;font-weight:600">wade@whcrafted.com</div></div></div>
      <div class="footer-row"><i class="ico" style="width:24px;height:24px"><svg style="width:13px;height:13px"><use href="#i-pin"/></svg></i><div><div style="font-size:11.5px;font-weight:600;line-height:1">MAIL:</div><div style="font-size:15px;font-weight:600;line-height:1.15">415 North Fernmill Rd,<br>Suite 308, Carmel IN 46033</div></div></div>
    </div>

    <footer class="site-footer" style="top:499px;height:254px">
      <div class="footer-brand"><span class="brand-square"></span><span class="brand-name">WADE HOLLORAN</span></div>
      <div class="quick-links" style="left:346px"><div class="footer-col-title">QUICK LINKS</div><ul><li>HOME</li><li>ABOUT</li><li>PROPERTIES</li><li>NEWS</li><li>BLOG</li><li>CONTACT</li></ul></div>
      <div class="footer-contact" style="left:469px"><div class="footer-col-title">CONTACT US</div>
        <div class="footer-row"><i class="ico"><svg><use href="#i-phone"/></svg></i><div><div class="f-label">PHONE:</div><div class="f-value">317-552-7190</div></div></div>
        <div class="footer-row"><i class="ico"><svg><use href="#i-mail"/></svg></i><div><div class="f-label">MAIL:</div><div class="f-value">wade@whcrafted.com</div></div></div>
        <div class="footer-row"><i class="ico"><svg><use href="#i-pin"/></svg></i><div><div class="f-label">MAIL:</div><div class="f-value">415 North Fernmill Rd,<br>Suite 308, Carmel IN 46033</div></div></div>
      </div>
      <div class="footer-bar">COPYRIGHT © WADE HOLLORAN 2023 . ALL RIGHTS RESERVED.</div>
    </footer>
  </section>

</div>
</body>
</html>
```